New Business Card for our Indoor Golf Training Facility

We are looking for designs for a new business card for our indoor golf training facility. Attached is our logo, our logo with our slogan, and here is our elevator pitch (What makes us different from the others) not sure if all the info will fit on one card, maybe you can condense the elevator pitch? here is the info

Elevator Pitch
We work with serious golfers and those that want to be serious golfers…
to make you better, faster, at all phases of the game…
We use the same state-of-the-art technology as professional golfers…
which produces data sets that shows your improvement in real time.
Our facility is available 24/7 to our members, which allows you to improve on your time.

our website: www.brambleteegolf.com

Target Market(s)

Golfers

Font styles to use
Serif
Sans Serif

Colors
ec1f27
f59195
fbd4d5
919191
d3d3d3
1b1b1b

Requirements
Must have
• our logo or our logo with the slogan, elevator pitch (can be condensed or shortened)

```html
<!DOCTYPE html>
<html lang="en">
<head>
<meta charset="utf-8">
<title>Bramble Tee Golf – Business Card</title>
<link href="https://fonts.googleapis.com/css2?family=Roboto:wght@400;700&family=Roboto+Condensed:ital,wght@0,400;0,700;1,400&display=swap" rel="stylesheet">
<style>
  :root {
    --red: #ec1f27;
    --red-card: #e23a33;
    --pink: #f59195;
    --blush: #fbd4d5;
    --grey: #919191;
    --light-grey: #d3d3d3;
    --ink: #1b1b1b;
    --text-grey: #555555;
    --paper: #f7f7f7;
    --backdrop: #e9e6e1;
    --white: #ffffff;
  }
  * { box-sizing: border-box; margin: 0; padding: 0; }
  html, body { width: 1200px; height: 911px; overflow: hidden; }
  body {
    background: var(--backdrop);
    font-family: "Roboto", Arial, sans-serif;
    position: relative;
  }
  .card {
    position: absolute;
    width: 580px;
    height: 330px;
    border-radius: 18px;
    box-shadow: 0 10px 28px rgba(0,0,0,.18);
    overflow: hidden;
  }

  /* Front */
  .card--front {
    left: 50px; top: 60px;
    background: var(--paper);
    border-top: 8px solid var(--red-card);
  }
  .brand { position: absolute; left: 44px; top: 52px; }
  .brand__name {
    font-weight: 700; font-size: 44px; line-height: 1;
    color: var(--red);
  }
  .brand__slogan {
    font-size: 16px; color: var(--red); margin-top: 8px;
  }
  .person { position: absolute; left: 44px; top: 176px; }
  .person__name {
    font-family: "Roboto Condensed", Arial, sans-serif;
    font-weight: 700; font-size: 24px; color: var(--red);
  }
  .person__role {
    font-family: "Roboto Condensed", Arial, sans-serif;
    font-size: 16px; color: var(--ink); margin-top: 2px;
  }
  .contacts {
    position: absolute; left: 44px; top: 240px;
    list-style: none; font-size: 14px; color: var(--text-grey);
  }
  .contacts li { display: flex; align-items: center; gap: 8px; height: 22px; }
  .contacts svg { width: 12px; height: 12px; fill: var(--red); }
  .divider {
    position: absolute; left: 290px; top: 236px;
    width: 1px; height: 66px; background: var(--light-grey);
  }
  .address {
    position: absolute; left: 310px; top: 246px;
    font-style: normal; font-size: 14px; line-height: 22px; color: var(--text-grey);
  }

  /* Back */
  .card--back {
    left: 570px; top: 520px;
    background: var(--red-card);
    color: var(--white);
    text-align: center;
  }
  .back__brand {
    position: absolute; left: 0; right: 0; top: 56px;
    font-weight: 700; font-size: 34px; line-height: 1;
  }
  .back__title {
    position: absolute; left: 0; right: 0; top: 140px;
    font-weight: 700; font-size: 19px; letter-spacing: .5px;
  }
  .back__pitch {
    position: absolute; left: 30px; right: 30px; top: 176px;
    font-family: "Roboto Condensed", Arial, sans-serif;
    font-style: italic; font-size: 13.5px; line-height: 20px;
  }
</style>
</head>
<body>
  <section class="card card--front" aria-label="Card front">
    <div class="brand">
      <div class="brand__name">Bramble Tee Golf</div>
      <div class="brand__slogan">Play Steady. Train Smarter. Go Lower Every Round.</div>
    </div>

    <div class="person">
      <div class="person__name">Owen Hale</div>
      <div class="person__role">CEO/Founder</div>
    </div>

    <ul class="contacts">
      <li>
        <svg viewBox="0 0 24 24" aria-hidden="true"><path d="M6.6 10.8a15.1 15.1 0 0 0 6.6 6.6l2.2-2.2a1 1 0 0 1 1-.25 11.4 11.4 0 0 0 3.6.57 1 1 0 0 1 1 1V20a1 1 0 0 1-1 1A17 17 0 0 1 3 4a1 1 0 0 1 1-1h3.5a1 1 0 0 1 1 1c0 1.25.2 2.45.57 3.57a1 1 0 0 1-.25 1z"/></svg>
        555-014-2290
      </li>
      <li>
        <svg viewBox="0 0 24 24" aria-hidden="true"><path d="M2 5h20v14H2z"/></svg>
        info@brambleteegolf.com
      </li>
      <li>
        <svg viewBox="0 0 24 24" aria-hidden="true"><circle cx="12" cy="12" r="11"/></svg>
        brambleteegolf.com
      </li>
    </ul>

    <span class="divider"></span>

    <address class="address">
      418 Linden Park RD Unit B4<br>
      Millbrook, OH 45000
    </address>
  </section>

  <section class="card card--back" aria-label="Card back">
    <div class="back__brand">Bramble Tee Golf</div>
    <h2 class="back__title">ELEVATOR PITCH :</h2>
    <p class="back__pitch">
      We coach committed players and anyone ready to commit to their game…<br>
      helping you improve quicker in every part of your round…<br>
      Our studio runs the same advanced tools the tour players rely on…<br>
      giving you clear numbers that track your progress as it happens.<br>
      Members have round-the-clock access, so you can practise whenever suits you.
    </p>
  </section>
</body>
</html>
```